Would like a Northwest feel to the look, something NOT typical of what you would see on a typical Home Inspectors logo. Real estate cards all the same as well, and would like to stand out. Earthy, green, Northwest. Sadly a portrait seems to be a requirement (see the attached). I inspect residential homes for buyers and sellers.

Target Market(s)

Home Buyers and Sellers

Industry/Entity Type

Home Inspection

Contact Information for Business Card

See description
Note: The name Varrowen is a Chinook word that means 'Friend'. Please do not associate the name with the Whale that shows up on 99% of google searches.

Logo Text

Varrowen Home Inspections

Colors

Designer to choose colors to be used in the design.

Requirements
Must have
• Phone Num: 541-276-8103
• Address: 712 SW 94th Av Num 318
• Portland, Oregon 97185
• Email: mark@varrowenhomeinspection.example
• Website: www.VarrowenHomeInspection.example
• Additional Note: Need to add the Bexolora logo (icon). It should be small and not the focus of the card. The logo can be found at Bexolora.example
Nice to have
• I am open
Should not have
• Cant think of anything

```html
<!DOCTYPE html>
<html lang="en">
<head>
<meta charset="utf-8">
<title>Varrowen Home Inspections – Business Cards</title>
<link rel="stylesheet" href="https://fonts.googleapis.com/css2?family=Open+Sans:wght@300;400;600&display=swap">
<style>
  :root {
    --page: #ecebe8;
    --forest: #3f4f4c;
    --forest-deep: #2f3b39;
    --paper: #f6f6f4;
    --paper-shade: #e4e4e1;
    --ink: #2b2b2b;
    --ink-soft: #6a6a6a;
    --sun: #e48a2c;
    --bar: #8a8a8a;
    --gold: #c9a640;
    --photo-a: #b9a99a;
    --photo-b: #7c8070;
  }
  * { box-sizing: border-box; margin: 0; padding: 0; }
  html, body { width: 1200px; height: 900px; overflow: hidden; }
  body {
    background: var(--page);
    font-family: "Open Sans", Arial, sans-serif;
    color: var(--ink);
    position: relative;
  }
  .card {
    position: absolute;
    width: 700px;
    height: 400px;
    left: 440px;
    border-radius: 4px;
    overflow: hidden;
    box-shadow: 0 6px 18px rgba(0,0,0,.18);
  }
  .mark-dot {
    border-radius: 50%;
    background: var(--sun);
    flex: none;
  }
  .brand-main { display: block; font-weight: 300; line-height: 1; }
  .brand-sub { display: block; font-weight: 300; line-height: 1.1; }

  /* Front */
  .card-front {
    top: 30px;
    background: linear-gradient(160deg, var(--forest) 0%, var(--forest-deep) 100%);
    color: #fff;
  }
  .front-mark {
    position: absolute;
    left: 70px; top: 110px;
    display: flex; align-items: center; gap: 30px;
  }
  .front-mark .mark-dot { width: 170px; height: 170px; }
  .front-name .brand-main { font-size: 58px; }
  .front-name .brand-sub { font-size: 27px; margin-top: 4px; }
  .front-web {
    font-weight: 300;
    font-size: 13px;
    margin-top: 8px;
    opacity: .9;
  }
  .cert-badge {
    position: absolute;
    right: 40px; bottom: 90px;
    width: 64px; height: 64px; border-radius: 50%;
    background: var(--gold);
  }

  /* Back */
  .card-back {
    top: 470px;
    background: linear-gradient(180deg, var(--paper) 0%, var(--paper-shade) 100%);
  }
  .back-band {
    position: absolute;
    left: 240px; right: 0; bottom: 0;
    height: 56px;
    background: var(--forest);
  }
  .portrait {
    position: absolute;
    right: 0; bottom: 56px;
    width: 290px; height: 240px;
    background: linear-gradient(160deg, var(--photo-a), var(--photo-b));
  }
  .person {
    position: absolute;
    right: 40px; top: 30px;
    text-align: right;
    padding-right: 16px;
    border-right: 10px solid var(--bar);
  }
  .person-name { font-size: 24px; font-weight: 400; line-height: 1.1; }
  .person-title { font-size: 15px; font-weight: 300; color: var(--ink-soft); }
  .back-mark {
    position: absolute;
    left: 40px; top: 36px;
    display: flex; align-items: center; gap: 16px;
  }
  .back-mark .mark-dot { width: 84px; height: 84px; }
  .back-name .brand-main { font-size: 32px; }
  .back-name .brand-sub { font-size: 15px; margin-top: 2px; }
  .contacts {
    position: absolute;
    left: 40px; bottom: 76px;
    list-style: none;
    font-size: 14px;
    line-height: 1.35;
  }
  .contacts li { display: flex; align-items: flex-start; gap: 12px; margin-top: 6px; }
  .contacts svg { width: 16px; height: 16px; flex: none; margin-top: 2px; fill: var(--ink-soft); }

  /* Standalone lockup */
  .lockup {
    position: absolute;
    left: 40px; top: 600px;
    width: 300px;
    text-align: center;
  }
  .lockup .mark-dot { width: 150px; height: 150px; margin: 0 auto 18px; }
  .lockup-name .brand-main { font-size: 56px; font-weight: 400; }
  .lockup-name .brand-sub { font-size: 24px; font-weight: 400; margin-top: 2px; }
</style>
</head>
<body>

  <section class="card card-front" aria-label="Business card front">
    <div class="front-mark">
      <span class="mark-dot"></span>
      <div>
        <p class="front-name"><span class="brand-main">Varrowen</span><span class="brand-sub">Home Inspections</span></p>
        <p class="front-web">www.VarrowenHomeInspection.example</p>
      </div>
    </div>
    <span class="cert-badge" role="img" aria-label="Bexolora certification badge"></span>
  </section>

  <section class="card card-back" aria-label="Business card back">
    <div class="portrait" role="img" aria-label="Portrait photo of the inspector"></div>
    <div class="back-band"></div>
    <div class="person">
      <p class="person-name">Your Name</p>
      <p class="person-title">Job Title</p>
    </div>
    <div class="back-mark">
      <span class="mark-dot"></span>
      <p class="back-name"><span class="brand-main">Varrowen</span><span class="brand-sub">Home Inspections</span></p>
    </div>
    <ul class="contacts">
      <li>
        <svg viewBox="0 0 24 24" aria-hidden="true"><path d="M6.6 10.8a15 15 0 0 0 6.6 6.6l2.2-2.2a1 1 0 0 1 1-.25 11.4 11.4 0 0 0 3.6.57 1 1 0 0 1 1 1V20a1 1 0 0 1-1 1A17 17 0 0 1 3 4a1 1 0 0 1 1-1h3.5a1 1 0 0 1 1 1c0 1.25.2 2.45.57 3.57a1 1 0 0 1-.25 1z"/></svg>
        <span>541-276-8103</span>
      </li>
      <li>
        <svg viewBox="0 0 24 24" aria-hidden="true"><path d="M2 5h20v14H2z M4 7v.4l8 5 8-5V7l-8 5z"/></svg>
        <span>mark@varrowenhomeinspection.example</span>
      </li>
      <li>
        <svg viewBox="0 0 24 24" aria-hidden="true"><path d="M12 2a7 7 0 0 0-7 7c0 5.2 7 13 7 13s7-7.8 7-13a7 7 0 0 0-7-7zm0 9.5A2.5 2.5 0 1 1 12 6.5a2.5 2.5 0 0 1 0 5z"/></svg>
        <span>712 SW 94th Av Num 318<br>Portland, Oregon 97185</span>
      </li>
    </ul>
  </section>

  <div class="lockup" aria-label="Logo lockup">
    <div class="mark-dot"></div>
    <p class="lockup-name"><span class="brand-main">Varrowen</span><span class="brand-sub">Home Inspections</span></p>
  </div>

</body>
</html>
```